A business card design for a dental office. We have Two doctors working here. We practice general de

I already have a logo designed for the office with the name and a slogan.
Now I need to create design for a business card using the same logo.
Details Needed on the front side of the card are :
Gregory L. Vanmerick, DDS
Daniel R Hoskett, DDS
418 Birchwood Lane
Milbrook, ME 04092
Phone : 207 555 0193
Fax : 207 555 0194
Website : WWW.BrightcrestDental.Com
Office hours by appointment
On the back side of the card need :
Appointment
Date....................Time...................
With....................................
If unable to keep your appointment, please give 24-48 hours notice in order to avoid broken appointment fee.

Industry/Entity Type

Dental Clinic

Contact Information for Business Card

Gregory L. Vanmerick, DDS
Daniel R Hoskett, DDS
418 Birchwood Lane
Milbrook, ME 04092
Phone : 207 555 0193
Fax : 207 555 0194
Appointment

Requirements
Must have
• Keep the Name and slogan on the logo on the front of the card. You can move them around the Logo and Name/Slogan of business (Vanmerick Family Dentistry/Every visit ends in a smile) as you wish to get a feel of the design.
• Gregory L. Vanmerick, DDS
• Daniel R Hoskett, DDS
• 418 Birchwood Lane
• Milbrook, ME 04092
• Phone : 207 555 0193
• Fax : 207 555 0194
• WWW.BrightcrestDental.Com
• Keep these three groups above as they are together now in different areas of the front side.
• On the back side of the card need :
• Appointment
• Date....................Time...................
• With....................................
• If unable to keep your appointment, please give 24-48 hours notice in order to avoid broken appointment fee.

```html
<!DOCTYPE html>
<html lang="en">
<head>
<meta charset="utf-8">
<title>Vanmerick Family Dentistry — Business Card</title>
<link rel="stylesheet" href="https://fonts.googleapis.com/css2?family=Cinzel:wght@700&family=Montserrat:wght@600;700&family=Roboto:wght@400&display=swap">
<style>
  :root {
    --backdrop: #161616;
    --card: #ffffff;
    --header-grey: #d0d1d0;
    --brand-blue: #1a5ea8;
    --curve-blue: #1d5fae;
    --slogan-red: #e0474c;
    --ink: #111111;
    --rule: #222222;
  }
  * { margin: 0; padding: 0; box-sizing: border-box; }
  html, body { width: 1189px; height: 1200px; overflow: hidden; }
  body { background: var(--backdrop); position: relative; font-family: "Roboto", Arial, sans-serif; }

  .card {
    position: absolute; left: 136px; width: 917px; height: 524px;
    background: var(--card); overflow: hidden;
  }
  .card--front { top: 45px; }
  .card--back { top: 623px; }

  .card-header { position: absolute; inset: 0; width: 917px; height: 524px; }

  .brand-mark {
    position: absolute; left: 133px; top: 24px; width: 144px; height: 144px;
    border-radius: 50%; background: var(--brand-blue);
  }
  .brand-name {
    position: absolute; left: 306px; top: 86px; width: 488px; text-align: center;
    font-family: "Montserrat", Arial, sans-serif; font-weight: 700;
    font-size: 27px; letter-spacing: 0.8px; color: var(--brand-blue); white-space: nowrap;
  }
  .brand-slogan {
    position: absolute; left: 352px; top: 128px; width: 392px;
    display: flex; align-items: center; gap: 10px;
    font-family: "Montserrat", Arial, sans-serif; font-weight: 600;
    font-size: 12.5px; letter-spacing: 2.4px; color: var(--slogan-red); white-space: nowrap;
  }
  .brand-slogan::before, .brand-slogan::after {
    content: ""; flex: 1; height: 1px; background: var(--slogan-red);
  }

  .doctor {
    position: absolute; left: 41px;
    font-family: "Cinzel", Georgia, serif; font-weight: 700;
    color: var(--brand-blue); letter-spacing: 2px; line-height: 1.2;
  }
  .doctor__name { font-size: 26px; white-space: nowrap; }
  .doctor__title { font-size: 20px; }
  .doctor--first { top: 292px; }
  .doctor--second { top: 385px; }

  .divider { position: absolute; left: 394px; top: 275px; width: 2px; height: 201px; background: var(--rule); }

  .contact-list { position: absolute; left: 418px; top: 277px; list-style: none; }
  .contact-list li {
    display: flex; align-items: center; gap: 16px; height: 49px;
    font-size: 25px; color: var(--ink); white-space: nowrap;
  }
  .contact-icon { width: 22px; height: 22px; flex: none; }

  .appointment-title {
    position: absolute; left: 346px; top: 160px; width: 346px; text-align: center;
    font-family: "Cinzel", Georgia, serif; font-weight: 700; font-size: 38px;
    letter-spacing: 4px; color: var(--brand-blue); white-space: nowrap;
  }

  .weekday { position: absolute; top: 240px; width: 80px; text-align: center; font-size: 27px; color: var(--ink); }
  .weekday__box {
    display: block; margin: 18px auto 0; width: 44px; height: 41px;
    border: 1px solid #555; background: #fff;
  }

  .form-label { position: absolute; font-size: 27px; color: var(--ink); white-space: nowrap; }
  .form-line { position: absolute; height: 3px; background: var(--ink); }
</style>
</head>
<body>

<section class="card card--front" aria-label="Business card front">
  <svg class="card-header" viewBox="0 0 917 524" aria-hidden="true">
    <path d="M0 0 H917 V147 Q432 290 0 163 Z" fill="var(--header-grey)"/>
    <path d="M0 163 Q432 290 917 147" fill="none" stroke="var(--curve-blue)" stroke-width="3"/>
  </svg>
  <div class="brand-mark" aria-hidden="true"></div>
  <div class="brand-name">VANMERICK FAMILY DENTISTRY</div>
  <div class="brand-slogan">EVERY VISIT ENDS IN A SMILE</div>

  <div class="doctor doctor--first">
    <div class="doctor__name">Gregory L. Vanmerick</div>
    <div class="doctor__title">DDS</div>
  </div>
  <div class="doctor doctor--second">
    <div class="doctor__name">Daniel R Hoskett</div>
    <div class="doctor__title">DDS</div>
  </div>

  <div class="divider"></div>

  <ul class="contact-list">
    <li>
      <svg class="contact-icon" viewBox="0 0 22 22" aria-label="Phone"><rect width="22" height="22" fill="var(--brand-blue)"/><path d="M7 5c-1 1-1 3 0 5s3 5 5 6 3 1 4 0l-2-3-2 1c-1-1-2-2-3-4l1-2z" fill="#fff"/></svg>
      207 555 0193
    </li>
    <li>
      <svg class="contact-icon" viewBox="0 0 22 22" aria-label="Fax"><rect width="22" height="22" fill="var(--brand-blue)"/><rect x="7" y="4" width="8" height="5" fill="#fff"/><rect x="4" y="9" width="14" height="6" fill="#fff"/><rect x="7" y="13" width="8" height="5" fill="#fff" stroke="var(--brand-blue)"/></svg>
      207 555 0194
    </li>
    <li>
      <svg class="contact-icon" viewBox="0 0 22 22" aria-label="Website"><rect width="22" height="22" fill="var(--brand-blue)"/><circle cx="11" cy="11" r="6.5" fill="none" stroke="#fff" stroke-width="1.6"/><path d="M4.5 11h13M11 4.5c-3 3-3 10 0 13M11 4.5c3 3 3 10 0 13" fill="none" stroke="#fff" stroke-width="1.2"/></svg>
      WWW.BrightcrestDental.Com
    </li>
    <li>
      <svg class="contact-icon" viewBox="0 0 22 22" aria-label="Address"><rect width="22" height="22" fill="var(--brand-blue)"/><path d="M11 18c-3-4-5-6-5-9a5 5 0 0 1 10 0c0 3-2 5-5 9z" fill="#fff"/><circle cx="11" cy="9" r="1.8" fill="var(--brand-blue)"/></svg>
      418 Birchwood Lane Milbrook, ME 04092
    </li>
  </ul>
</section>

<section class="card card--back" aria-label="Business card back">
  <svg class="card-header" viewBox="0 0 917 524" aria-hidden="true">
    <path d="M0 0 H917 V147 Q432 290 0 163 Z" fill="var(--header-grey)"/>
    <path d="M0 163 Q432 290 917 147" fill="none" stroke="var(--curve-blue)" stroke-width="3"/>
  </svg>
  <div class="brand-mark" aria-hidden="true"></div>
  <div class="brand-name">VANMERICK FAMILY DENTISTRY</div>
  <div class="brand-slogan">EVERY VISIT ENDS IN A SMILE</div>
  <div class="appointment-title">APPOINTMENT</div>

  <div class="weekday" style="left:124px">MON<span class="weekday__box"></span></div>
  <div class="weekday" style="left:220px">TUE<span class="weekday__box"></span></div>
  <div class="weekday" style="left:323px">WED<span class="weekday__box"></span></div>
  <div class="weekday" style="left:421px">THU<span class="weekday__box"></span></div>
  <div class="weekday" style="left:519px">FRI<span class="weekday__box"></span></div>
  <div class="weekday" style="left:614px">SAT<span class="weekday__box"></span></div>
  <div class="weekday" style="left:715px">SUN<span class="weekday__box"></span></div>

  <div class="form-label" style="left:47px;top:358px">Date :-</div>
  <div class="form-line" style="left:149px;top:374px;width:248px"></div>
  <div class="form-label" style="left:414px;top:356px">Time :-</div>
  <div class="form-line" style="left:512px;top:374px;width:248px"></div>
  <div class="form-label" style="left:771px;top:354px">am/pm</div>

  <div class="form-label" style="left:47px;top:411px">Date :-</div>
  <div class="form-line" style="left:149px;top:427px;width:248px"></div>
  <div class="form-label" style="left:414px;top:411px">Time :-</div>
  <div class="form-line" style="left:512px;top:427px;width:248px"></div>
  <div class="form-label" style="left:771px;top:408px">am/pm</div>

  <div class="form-label" style="left:271px;top:466px">With :-</div>
  <div class="form-line" style="left:370px;top:483px;width:250px"></div>
</section>

</body>
</html>
```